This book will apply the 12 Steps to gaming addiction, also known as video game addiction. The primary purpose of the book is to provide an effective solution for this new type of addiction. The solution is based on the rich and successful concepts of traditional twelve-step programs like RL.

The title on the cover will be "Nine Doors Past the Glowing Screen" and "by Martin Quorby". A subtitle can be used if it works in your design of "A Practical Path Beyond Compulsive Console Play". Cover will be for a 6" x 9" book approximately 110 pages in length.

Some back cover text including some review quotes and an author bio are in the attached Word doc. There is also an author photo attached for for the back cover.

Requirements
Must have
• For the cover design it could be stylized, or an image, a partial image, or whatever. I am open to suggestions. Think about what would be noticed by a person searching for help with moderating their video game use, or by the parents or loved ones of problem gamers. Something contemporary and eye catching.

```html
<!DOCTYPE html>
<html lang="en">
<head>
<meta charset="utf-8">
<title>Nine Doors Past the Glowing Screen — Cover Spread</title>
<link rel="stylesheet" href="https://fonts.googleapis.com/css2?family=Saira+Condensed:wght@500;600;700&family=Poppins:wght@400;600;700&display=swap">
<style>
  :root {
    --page: #ffffff;
    --ink: #0b0b10;
    --text: #e9e9ee;
    --text-dim: #c9c9d2;
    --orange: #ff8a4c;
    --orange-light: #ffb37a;
    --pink: #ff7aa8;
    --violet: #9a8cff;
    --blue: #7f9bf0;
    --steel: #8ea4d6;
    --rule: #5a5a66;
    --display: "Saira Condensed", "Arial Narrow", sans-serif;
    --body: "Poppins", Arial, sans-serif;
  }
  * { box-sizing: border-box; margin: 0; padding: 0; }
  html, body { width: 1200px; height: 1000px; overflow: hidden; background: var(--page); }
  .canvas { position: relative; width: 1200px; height: 1000px; background: var(--page); }

  .spread {
    position: absolute; left: 190px; top: 0; width: 985px; height: 730px;
    background: var(--ink); overflow: hidden;
  }

  /* back cover */
  .back { position: absolute; left: 0; top: 0; width: 450px; height: 730px; }
  .back-art {
    position: absolute; left: 0; top: 330px; width: 450px; height: 400px;
    background:
      radial-gradient(circle at 10% 28%, rgba(255,255,255,.55) 0 3%, rgba(120,110,255,.25) 9%, transparent 22%),
      radial-gradient(ellipse at 20% 40%, rgba(80,70,200,.35), transparent 45%),
      linear-gradient(180deg, transparent, rgba(20,20,40,.4));
    opacity: .85;
  }
  .back-copy {
    position: absolute; left: 82px; top: 94px; width: 336px;
    font-family: var(--body); color: var(--text); font-size: 8.3px; line-height: 1.38;
  }
  .praise-heading {
    font-family: var(--display); font-weight: 600; font-size: 15.5px; letter-spacing: .4px;
    color: #fff; margin-bottom: 13px; white-space: nowrap;
  }
  .praise-heading .accent { color: var(--orange); }
  .review { font-weight: 600; margin-bottom: 18px; }
  .review cite { display: block; font-style: normal; font-weight: 600; color: var(--text); }
  .review cite .who { color: var(--steel); }
  .divider { border: 0; border-top: 1px solid var(--rule); margin: 4px 0 14px; }
  .blurb p { margin-bottom: 9px; color: var(--text-dim); }
  .author-bio { display: flex; gap: 10px; margin-top: 14px; font-size: 8.3px; }
  .author-photo {
    flex: 0 0 58px; height: 72px;
    background: linear-gradient(160deg, #8e94a8, #3c4358 60%, #23283a);
  }
  .author-bio p { color: var(--text-dim); }
  .author-bio .name { font-family: var(--display); color: var(--orange); font-size: 11px; font-weight: 600; }

  /* spine */
  .spine { position: absolute; left: 450px; top: 0; width: 60px; height: 730px; }
  .spine-title, .spine-author {
    position: absolute; left: 50%; transform: translateX(-50%);
    writing-mode: vertical-rl; font-family: var(--display); font-weight: 600; white-space: nowrap;
  }
  .spine-title {
    top: 92px; font-size: 16px; letter-spacing: 4.5px;
    background: linear-gradient(180deg, var(--orange-light), var(--pink) 45%, var(--blue));
    -webkit-background-clip: text; background-clip: text; color: transparent;
  }
  .spine-author { top: 525px; font-size: 20px; letter-spacing: 2px; color: var(--orange); }

  /* front cover */
  .front { position: absolute; left: 510px; top: 0; width: 475px; height: 730px; overflow: hidden; }
  .front-art {
    position: absolute; inset: 0;
    background:
      radial-gradient(circle at 78% 60%, #ffffff 0 5%, rgba(200,190,255,.8) 8%, rgba(120,100,255,.35) 16%, transparent 30%),
      radial-gradient(ellipse at 65% 72%, rgba(90,120,230,.65), transparent 40%),
      radial-gradient(ellipse at 35% 62%, rgba(255,70,120,.45), transparent 32%),
      radial-gradient(ellipse at 60% 30%, rgba(60,160,220,.45), transparent 38%),
      linear-gradient(180deg, #07070c 0%, #111428 40%, #1a2150 70%, #0c0c14 100%);
  }
  .title-lines { position: absolute; left: 0; top: 0; }
  .title { position: absolute; left: 0; top: 0; width: 475px; height: 360px; font-family: var(--display); }
  .title span { position: absolute; line-height: 1; white-space: nowrap; font-weight: 700; }
  .title .nine { left: 62px; top: 98px; font-size: 40px; font-weight: 600; color: #fff; }
  .title .doors, .title .past, .title .the {
    left: 58px;
    background: linear-gradient(180deg, var(--orange-light), var(--orange));
    -webkit-background-clip: text; background-clip: text; color: transparent;
  }
  .title .doors { top: 148px; font-size: 48px; }
  .title .past { top: 204px; font-size: 60px; }
  .title .the { top: 270px; font-size: 60px; }
  .title .glow {
    left: 196px; font-size: 76px;
    background: linear-gradient(90deg, var(--orange-light), var(--pink) 45%, var(--violet));
    -webkit-background-clip: text; background-clip: text; color: transparent;
  }
  .title .glow.one { top: 152px; }
  .title .glow.two {
    top: 236px;
    background: linear-gradient(90deg, var(--pink), var(--violet) 50%, var(--blue));
    -webkit-background-clip: text; background-clip: text;
  }
  .cover-quote {
    position: absolute; left: 58px; top: 372px; width: 220px; white-space: nowrap;
    font-family: var(--body); font-weight: 600; font-size: 15px; line-height: 1.3; color: #fff;
  }
  .cover-credit { position: absolute; left: 58px; top: 500px; font-family: var(--body); font-size: 11px; line-height: 1.3; color: #fff; }
  .cover-credit .who { font-weight: 700; color: var(--steel); display: block; }
  .cover-author {
    position: absolute; left: 56px; top: 582px; font-family: var(--display); font-weight: 700;
    font-size: 62px; letter-spacing: 2px; line-height: 1; color: var(--orange); white-space: nowrap;
  }
</style>
</head>
<body>
<div class="canvas">
  <section class="spread">

    <article class="back">
      <div class="back-art" role="img" aria-label="Faded continuation of the glowing headset artwork"></div>
      <div class="back-copy">
        <h2 class="praise-heading">PRAISE FOR <span class="accent">NINE DOORS PAST THE GLOWING SCREEN</span></h2>

        <blockquote class="review">
          “A must-read for anyone who is addicted to or thinks they may have a problem with digital gaming. This eloquent work will also be useful to academics and clinicians exploring potential solutions. The author recognizes the similarities between gaming addiction and other addictions, and logically applies one of the most effective known solutions for addiction - The Twelve Steps.”
          <cite><span class="who">DALE WHITCOMBE,</span> Noted Interventionist and Keynote Speaker</cite>
        </blockquote>

        <blockquote class="review">
          “If you suffer from digital gaming addiction, I strongly encourage you to use this book as your road map to get you back to the real world.”
          <cite><span class="who">RENATA OLFIELD,</span> Founder of Signal Street Review.</cite>
        </blockquote>

        <blockquote class="review">
          “As a high school teacher for 24 years, husband, father, coach, and 12-Step member, I can assure you that this book will transform the life of anyone who is addicted to video games. Well written, easy to understand, and a wonderful book that will provide you with a clear road map to recovery, and this includes teenagers, a group I have been working with in the classroom for decades.”
          <cite><span class="who">TOMAS FERROW, HARBOR VALE,</span> CA High School Teacher.</cite>
        </blockquote>

        <hr class="divider">

        <div class="blurb">
          <p>A practical path beyond compulsive console play, based on the rich and successful tradition of the Twelve Steps.</p>
          <p>Addiction to Digital Gaming is a new and troubling phenomenon that has burst upon an unprepared society with alarming speed. Many people crave the use of Digital Games in a strikingly similar way to any other addict. Digital Games are a complex software and hardware system that have been designed to promote continued and progressive usage. This sophisticated technology clearly feeds on natural addictive tendencies.</p>
          <p>THE 12 STEPS are one of the most effective methods for treating addiction in human history. Originating with RL in 1939, the 12 Steps have since been used to treat a variety of other addictions, including drugs, sex, gambling, eating disorders, and many others. Now in this groundbreaking work the 12 Steps are applied to the complex and evolving contemporary phenomenon of Digital Gaming Addiction.</p>
        </div>

        <div class="author-bio">
          <div class="author-photo" role="img" aria-label="Author portrait photograph"></div>
          <p><span class="name">MARTIN QUORBY</span> is a Technology Consultant and Writer with many years of professional coding and consulting experience. He also struggled with addiction to drugs and alcohol and is now clean and sober in a Twelve-Step program for over 17 years. This unique combination of 12-Step experience and technology expertise led him to write Nine Doors Past the Glowing Screen.</p>
        </div>
      </div>
    </article>

    <aside class="spine">
      <span class="spine-title">NINE DOORS PAST THE GLOWING SCREEN</span>
      <span class="spine-author">MARTIN QUORBY</span>
    </aside>

    <article class="front">
      <div class="front-art" role="img" aria-label="Person wearing a glowing virtual reality headset bathed in blue and pink light with streams of code"></div>

      <svg class="title-lines" width="475" height="360" viewBox="0 0 475 360" aria-hidden="true">
        <g stroke="#9fb0e8" stroke-width="1.3" fill="none">
          <line x1="48" y1="118" x2="58" y2="118"/>
          <line x1="150" y1="118" x2="186" y2="118"/>
          <polyline points="186,118 186,348 360,348"/>
          <line x1="186" y1="143" x2="208" y2="143"/>
        </g>
        <circle cx="210" cy="143" r="6" fill="#9fb0e8"/>
        <circle cx="360" cy="348" r="6" fill="#9fb0e8"/>
      </svg>

      <h1 class="title">
        <span class="nine">NINE</span>
        <span class="doors">DOORS</span>
        <span class="past">PAST</span>
        <span class="the">THE</span>
        <span class="glow one">GLOWING</span>
        <span class="glow two">SCREEN</span>
      </h1>

      <p class="cover-quote">“A must-read for<br>anyone who is<br>addicted to or<br>thinks they may<br>have a problem<br>with digital gaming…”</p>
      <p class="cover-credit"><span class="who">DALE WHITCOMBE</span>Noted Interventionist<br>and Keynote Speaker</p>
      <p class="cover-author">MARTIN QUORBY</p>
    </article>

  </section>
</div>
</body>
</html>
```